Personal Development Brand Needs a Workbook Cover Design

We need a clean and sleek cover design for our A4-Sized workbook called the "12-Week Horizon Logbook"

There's around 90 pages in the workbook, if that matters for the spine.

Necessary Elements on the Front Cover:

- Logo
- Title: Peak Lantern Horizon Logbook
- Subtitle: A Simple Workbook to Track Your Transformation
- Author Name: Dale Wrenfold

Elements on Back Cover:

- The Peak Lantern Creed

```html
<!DOCTYPE html>
<html lang="en">
<head>
<meta charset="utf-8">
<title>Peak Lantern Horizon Logbook — Cover</title>
<link rel="stylesheet" href="https://fonts.googleapis.com/css2?family=Bebas+Neue&family=Montserrat:wght@600&display=swap">
<style>
  :root {
    --navy: #1f2133;
    --navy-deep: #191b2b;
    --glow-blue: #1d4a6e;
    --figure-cyan: #4fc3d9;
    --title-white: #f1f1f1;
    --title-red: #b8141d;
    --subtitle-white: #e4e4e4;
  }
  html, body {
    margin: 0;
    padding: 0;
    overflow: hidden;
    background: var(--navy-deep);
  }
  .cover {
    position: relative;
    width: 849px;
    height: 1200px;
    overflow: hidden;
    background:
      radial-gradient(ellipse 480px 700px at 120px 620px, var(--glow-blue) 0%, rgba(29,74,110,0.35) 45%, rgba(31,33,51,0) 80%),
      var(--navy);
  }
  .cover__figure {
    position: absolute;
    left: -40px;
    top: 0;
    width: 330px;
    height: 1200px;
    background:
      radial-gradient(ellipse 120px 560px at 140px 600px, rgba(79,195,217,0.45) 0%, rgba(79,195,217,0.18) 55%, rgba(79,195,217,0) 100%);
  }
  .cover__title,
  .cover__subtitle {
    margin: 0;
  }
  .title-line,
  .subtitle-line,
  .author {
    position: absolute;
    left: 0;
    width: 849px;
    margin: 0;
    text-align: center;
    line-height: 1;
    white-space: nowrap;
    box-sizing: border-box;
  }
  .title-line {
    display: block;
    padding-left: 24px;
    font-family: "Bebas Neue", sans-serif;
    font-weight: 400;
  }
  .title-line--brand {
    top: 206px;
    font-size: 130px;
    color: var(--title-white);
  }
  .title-line--horizon {
    top: 338px;
    font-size: 100px;
    color: var(--title-red);
  }
  .title-line--logbook {
    top: 440px;
    font-size: 196px;
    color: var(--title-red);
  }
  .subtitle-line {
    display: block;
    padding-left: 24px;
    font-family: "Bebas Neue", sans-serif;
    font-size: 46px;
    letter-spacing: 0.04em;
    color: var(--subtitle-white);
  }
  .subtitle-line--first { top: 692px; }
  .subtitle-line--second { top: 747px; }
  .author {
    top: 1061px;
    padding-left: calc(30px + 0.3em);
    font-family: "Montserrat", sans-serif;
    font-weight: 600;
    font-size: 50px;
    letter-spacing: 0.3em;
    color: var(--title-white);
  }
</style>
</head>
<body>
  <main class="cover">
    <div class="cover__figure" role="img" aria-label="Glowing cyan wireframe network illustration of a standing human figure"></div>

    <h1 class="cover__title">
      <span class="title-line title-line--brand">Peak Lantern</span>
      <span class="title-line title-line--horizon">Horizon</span>
      <span class="title-line title-line--logbook">Logbook</span>
    </h1>

    <p class="cover__subtitle">
      <span class="subtitle-line subtitle-line--first">A Simple Workbook to Track</span>
      <span class="subtitle-line subtitle-line--second">Your Transformation</span>
    </p>

    <p class="author">DALE WRENFOLD</p>
  </main>
</body>
</html>
```